RM Cargoline businesscard project

RM Cargoline Ltd is a freshly founded small (3 employees), young (average age is 30 years) company, living from the road transportation market without own tools.
We would like to have an impressive, new-line, cool busines card for a freshly founded forwarding company on an overcrowded market which raises attention and makes the potential partners eager to work with us.

Target Market(s)

The main profile of the company is logistic/forwarding on road.

Industry/Entity Type

Freight Forwarding

Contact Information for Business Card

Name: Berki Zsófia
Title: general manager
mobile nr: +36-70/482-5193
fax nr: +36-1/534-9061
e-mail: zsofia.berki@rmcargoline.example
info@rmcargoline.example
website address: http://www.rmcargoline.example
and if possible maybe some funny or helpful info on the back

Requirements
Must have
• contact details above
Nice to have
• some really nice and catching back-side (info, graphics, useful tool info... anything)
Should not have
• trucks, road, ship, airplane on it...

```html
<!DOCTYPE html>
<html lang="hu">
<head>
<meta charset="utf-8">
<title>RM Cargoline – Business Card</title>
<link rel="stylesheet" href="https://fonts.googleapis.com/css2?family=Jost:wght@400;500&display=swap">
<style>
  :root {
    --backdrop: #3d3d3d;
    --card-blue: #5781b8;
    --card-white: #f7f7f7;
    --ink-light: #ffffff;
    --ink-dark: #2b2b2b;
  }
  * { margin: 0; padding: 0; box-sizing: border-box; }
  html, body {
    width: 1200px; height: 750px; overflow: hidden;
    background: var(--backdrop);
    font-family: "Jost", "Futura", sans-serif;
  }
  .canvas { position: relative; width: 1200px; height: 750px; }
  .card {
    position: absolute; left: 371px; width: 461px; height: 263px; overflow: hidden;
  }
  .card--front { top: 114px; background: var(--card-blue); color: var(--ink-light); }
  .card--back { top: 402px; background: var(--card-white); }

  .front-corner { position: absolute; left: 0; top: 0; }

  .contact-block {
    position: absolute; right: 32px; top: 26px; text-align: right;
  }
  .person-name { font-size: 17px; font-weight: 500; letter-spacing: 0.6px; line-height: 20px; }
  .person-title { font-size: 13px; font-weight: 400; letter-spacing: 0.5px; line-height: 17px; }
  .contact-list { list-style: none; margin-top: 14px; }
  .contact-list li {
    display: flex; justify-content: flex-end; align-items: center;
    font-size: 12px; line-height: 18.5px; letter-spacing: 0.2px;
  }
  .contact-list svg { width: 14px; height: 14px; margin-left: 8px; flex: none; }

  .front-wordmark {
    position: absolute; right: 32px; top: 190px;
    font-size: 36px; font-weight: 500; letter-spacing: -0.5px; line-height: 44px;
  }

  .back-brand {
    position: absolute; inset: 0;
    display: flex; justify-content: center; align-items: center; gap: 10px;
  }
  .back-brand .brand-square { width: 22px; height: 22px; background: var(--card-blue); }
  .back-brand .brand-name {
    font-size: 34px; font-weight: 500; letter-spacing: -0.5px; color: var(--ink-dark);
  }
</style>
</head>
<body>
<main class="canvas">
  <section class="card card--front" aria-label="Business card front">
    <svg class="front-corner" width="180" height="195" viewBox="0 0 180 195" aria-hidden="true">
      <polygon points="0,0 178,0 0,192" fill="var(--card-white)"/>
    </svg>

    <div class="contact-block">
      <p class="person-name">Berki Zsófia</p>
      <p class="person-title">General Manager</p>
      <ul class="contact-list">
        <li>+36-70/482-5193
          <svg viewBox="0 0 14 14" aria-label="mobile"><rect x="4" y="1" width="7" height="12" rx="1.2" fill="none" stroke="#fff" stroke-width="1.4"/></svg>
        </li>
        <li>+36-1/534-9061
          <svg viewBox="0 0 14 14" aria-label="fax"><rect x="4" y="2" width="6" height="4" fill="#fff"/><rect x="1" y="6" width="12" height="6" rx="1" fill="#fff"/></svg>
        </li>
        <li>zsofia.berki@rmcargoline.example
          <svg viewBox="0 0 14 14" aria-label="email"><rect x="1" y="3" width="12" height="8" fill="#fff"/><polyline points="1,3 7,8 13,3" fill="none" stroke="var(--card-blue)" stroke-width="1"/></svg>
        </li>
        <li>info@rmcargoline.example
          <svg viewBox="0 0 14 14" aria-label="email"><rect x="1" y="3" width="12" height="8" fill="#fff"/><polyline points="1,3 7,8 13,3" fill="none" stroke="var(--card-blue)" stroke-width="1"/></svg>
        </li>
        <li>www.rmcargoline.example
          <svg viewBox="0 0 14 14" aria-label="website"><circle cx="7" cy="7" r="6" fill="#fff"/><path d="M4 5 Q7 4 8 7 Q6 9 7 12" fill="none" stroke="var(--card-blue)" stroke-width="1.2"/></svg>
        </li>
      </ul>
    </div>

    <p class="front-wordmark">RM Cargoline</p>
  </section>

  <section class="card card--back" aria-label="Business card back">
    <div class="back-brand">
      <span class="brand-square"></span>
      <span class="brand-name">RM Cargoline</span>
    </div>
  </section>
</main>
</body>
</html>
```